Norwegian psychologist service needs a fresh and exiting web site*

Norwegian psychologist service: working with therapy, personal development, mastery and personal growth. Focus: children and teenagers with special needs; family dynamics; group processes; individuals with a need for therapy and personal growth. (Our company name: Fjordlys og samhold (means Mastery and Growth).

We already have a logo for the company, which will be used (will be attached in the project).

The webside is to be structured in 4 pages with roll down curtain menus (the numbers are just for guiding the designer - the should not be added):

Page 1: Om Fjordlys og Samhold (about Mastery and Growth): this is where our business is is presented/described shortly: Lorem Ipsum dolor cit...

Page 2: Tjenester (Services): this is where our 5 service areas are presented:
2.1 Utredning (Investigation, diagnosing): Lorem Ipsum dolor cit...
2.2 Rådgivning (consulting): Lorem Ipsum dolor cit...

2.3 Kurs og work shops (courses and work shops): Lorem Ipsum dolor cit...
2.3a Fjordlys og samhold Tema 1 (T1)
2.3b Fjordlys og samhold Tema 2 (T2)
2.3c Fjordlys og samhold Tema 3 (T3)

2.4 Terapi og utvikling (Therapy and development)
2.4a Fjordlys og samhold for individer (FS1)
2.4b Fjordlys og samhold i familier (FS2)
2.4c Fjordlys og samhold i grupper (FS3)
2.4d Fjordlys og samhold i institusjoner (FS4)

Page 3: Aktuelt (Blog): this is our blog where we share knowledge and articles

Page 4: Kontakt (Contact): This is the contact form page. Contact form should constitute:
- Ditt navn (your name)
- E-post (your e-mail)
- Emne (subject)
- Melding (message/description)

Our project should also include suggestion for handheld units (iPhone, iPad).
Updates

We have both been traveling with work for a while, and then unfortunately both of us got sick on return, so we need a few more days to evaluate and choose design. Kind Regards Arvid & Margit

Target Market(s)

Focus on therapy, learning, mastery and growth for children and teenagers with special needs, within the family dynamics, or in a group setting.
OUR MARKETS:
Private market: individuals, families, groups and health industry institutions (with focus on learning, mastery, growth (as well as growing up) and psychiatry for children and teenagers with special difficulties and needs)
Public institutions: Government institutions, state institutions and municipality institutions (e.g. schools, municipality health service, hospitals) that serve the public (families with children and teenagers with special needs, and where learning, mastery, growth (as well as growing up) and potential psychiatry is an issue).

Number of Pages Required

4 page

Font styles to use
Sans Serif

Colors

Designer to choose colors to be used in the design.

Requirements
Must have
• The website must have 4 pages with roll down curtain menus (we have added a PDF with suggested structure, and headings, with sub menus - see attached PDF drawing.
• The web page must also use the added logo file - and make the web page work well with our logo.
• We would like the website to have a modern look and we would like the site to be associated with typical HIGH END TOP QUALITY private health institutions, but with a stronger focus on human beings (hands, faces etc), and not white coats and doctors. We are psychologists in the private market.
• For instance, if photos are being used - we tend to like "warm" almost art-like, "grainy" two-tone (e.g. sepia) photos to illustrate our focus. If designer can find such photos as part of design, it would be interesting to us. We would like a few photos like that integrated in the design.
• We also want a design suggestion for how the web page should look like and behave on handheld units (e.g. iPhone, iPad).
Nice to have
• If designer could find a number of suitable photos that matches the business idea and design requirements (see description above), that could follow website, that would be good.
• It could also be nice to have graphic symbols that denote the different pages/subpages (subjects)....
• HORSES: we sometimes use horses as a "tool" in therapy sessions. The horse is not necessarily used for riding, but for contact, communication and grooming. PHOTOS: we would like the designer to find an opportunity for using a photo reflecting this cooperation between therapist, child, teenager and horse. It is a bit up to the designer to find a way to do this... Since the horse is only a tool, among many other tools, it does not have to be much - but we want to try and see how it will work with a photo that also reflects this part of our business.

```html
<!DOCTYPE html>
<html lang="no">
<head>
<meta charset="utf-8">
<title>Tjenester – Fjordlys og samhold</title>
<link rel="stylesheet" href="https://fonts.googleapis.com/css2?family=Poppins:wght@300;400;500;600;700&display=swap">
<style>
  :root {
    --navy: #283891;
    --green: #056a3a;
    --green-dark: #04562f;
    --ink: #2b2b2b;
    --white: #ffffff;
    --mint: #e3f0ee;
    --mint-soft: #eef6f4;
    --icon-tint: rgba(255,255,255,0.22);
  }
  * { margin: 0; padding: 0; box-sizing: border-box; }
  html, body { width: 1200px; height: 800px; overflow: hidden; }
  body {
    position: relative;
    background: var(--white);
    font-family: "Poppins", sans-serif;
    color: var(--ink);
  }
  .backdrop { position: absolute; inset: 0; pointer-events: none; }
  .brand {
    position: absolute; left: 67px; top: 22px;
    display: flex; flex-direction: column; align-items: center; gap: 10px;
    width: 140px;
  }
  .brand-dot { width: 46px; height: 46px; border-radius: 50%; background: var(--navy); }
  .brand-name {
    font-size: 15px; font-weight: 500; color: var(--navy);
    text-align: center; line-height: 1.15; letter-spacing: 0.5px;
  }
  .main-nav {
    position: absolute; top: 44px; right: 66px;
    display: flex; align-items: center; gap: 32px;
    font-size: 13.5px; font-weight: 500; color: var(--ink);
  }
  .main-nav a { color: inherit; text-decoration: none; position: relative; }
  .main-nav a.is-active { color: var(--green); }
  .main-nav a.is-active::after {
    content: ""; position: absolute; left: 50%; bottom: -9px;
    width: 22px; height: 3px; border-radius: 2px;
    background: var(--green); transform: translateX(-50%);
  }
  .lang { display: flex; align-items: center; gap: 6px; font-size: 12.5px; margin-left: -4px; }
  .lang-flag {
    width: 26px; height: 26px; border-radius: 50%;
    background: linear-gradient(#c9303d 0 50%, #f2f2f2 50%);
    box-shadow: 0 2px 4px rgba(0,0,0,0.25);
  }
  .page-title {
    position: absolute; top: 140px; left: 0; width: 1200px;
    text-align: center; font-size: 44px; font-weight: 600;
    color: var(--navy); letter-spacing: 1px;
  }
  .service {
    position: absolute; top: 228px; width: 255px; height: 395px;
    background: var(--navy); color: var(--white);
    padding: 0 14px 0 22px;
    overflow: hidden;
  }
  .service--featured {
    top: 211px; height: 434px; background: var(--green);
    border-bottom: 4px solid var(--green-dark);
  }
  .service-icon {
    margin-top: 28px; width: 88px; height: 88px; border-radius: 10px;
    background: var(--icon-tint);
  }
  .service--featured .service-icon { margin-top: 45px; }
  .service h2 { margin-top: 22px; font-size: 18px; font-weight: 600; letter-spacing: 0.2px; }
  .service p {
    margin-top: 18px; font-size: 14px; line-height: 18px; font-weight: 300;
    letter-spacing: -0.1px;
  }
  .service ul { list-style: none; margin-top: 22px; }
  .service li {
    font-size: 13px; line-height: 21px; font-weight: 300; letter-spacing: -0.15px;
    position: relative; padding-left: 13px;
  }
  .service li::before {
    content: ""; position: absolute; left: 0; top: 7px;
    width: 8px; height: 8px; border: 2px solid var(--white); border-radius: 50%;
  }
  .leaf-art {
    position: absolute; right: 0; bottom: 0; width: 220px; height: 200px;
    background: radial-gradient(ellipse at 70% 60%, rgba(255,255,255,0.12), rgba(255,255,255,0) 70%);
  }
  .pager { position: absolute; left: 23px; top: 730px; display: flex; align-items: baseline; gap: 8px; }
  .pager-arrow { width: 22px; height: 14px; margin-right: 20px; align-self: center; }
  .pager-current { font-size: 56px; font-weight: 600; color: var(--ink); line-height: 1; }
  .pager-total { font-size: 20px; font-weight: 500; color: var(--ink); }
</style>
</head>
<body>
  <svg class="backdrop" width="1200" height="800" role="img" aria-label="Soft mint mountain landscape">
    <path d="M820 230 C900 180 960 160 1020 140 C1060 110 1100 90 1130 80 C1160 95 1190 110 1200 120 L1200 800 L960 800 C990 760 1000 700 960 660 C930 630 870 610 860 560 C850 500 900 440 880 380 C860 320 800 280 820 230 Z" fill="var(--mint-soft)"/>
    <path d="M900 230 C960 200 1020 170 1060 150 C1100 130 1130 100 1150 85 C1175 100 1195 120 1200 130 L1200 560 C1150 520 1090 470 1020 420 C960 380 920 300 900 230 Z" fill="var(--mint)"/>
  </svg>

  <header>
    <div class="brand">
      <span class="brand-dot"></span>
      <span class="brand-name">FJORDLYS OG SAMHOLD</span>
    </div>
    <nav class="main-nav">
      <a href="#">OM FJORDLYS OG SAMHOLD</a>
      <a href="#" class="is-active">TJENESTER</a>
      <a href="#">AKTUELT</a>
      <a href="#">KONTAKT</a>
      <span class="lang"><span class="lang-flag"></span>ENG
        <svg width="8" height="6" viewBox="0 0 8 6"><path d="M1 1l3 3 3-3" stroke="#2b2b2b" stroke-width="1.5" fill="none"/></svg>
      </span>
    </nav>
  </header>

  <h1 class="page-title">TJENESTER</h1>

  <section class="service" style="left:67px">
    <div class="service-icon" role="img" aria-label="Icon: documents with magnifying glass"></div>
    <h2>UTREDNING</h2>
    <p>Consectetur adipiscing elit cras sed aliquet m dignissim vamus dolor ligula egestas</p>
  </section>

  <section class="service service--featured" style="left:337px">
    <div class="service-icon" role="img" aria-label="Icon: people talking at a table"></div>
    <h2>RÅDGIVNING</h2>
    <p>Consectetur adipiscing elit cras sed aliquet m dignissim vamus dolor ligula egestas</p>
    <div class="leaf-art" role="img" aria-label="Faint leaf pattern"></div>
  </section>

  <section class="service" style="left:608px">
    <div class="service-icon" role="img" aria-label="Icon: presenter with audience"></div>
    <h2>KURS OG WORKSHOPS</h2>
    <p>Consectetur adipiscing elit cras sed aliquet m dignissim vamus dolor ligula egestas</p>
    <ul>
      <li>Fjordlys og samhold Tema 1</li>
      <li>Fjordlys og samhold Tema 2</li>
      <li>Fjordlys og samhold Tema 3</li>
    </ul>
  </section>

  <section class="service" style="left:878px">
    <div class="service-icon" role="img" aria-label="Icon: therapy conversation"></div>
    <h2>TERAPI OG UTVIKLING</h2>
    <p>Consectetur adipiscing elit cras sed aliquet m dignissim vamus dolor ligula egestas</p>
    <ul>
      <li>Fjordlys og samhold for individer</li>
      <li>Fjordlys og samhold i familier</li>
      <li>Fjordlys og samhold i grupper</li>
      <li>Fjordlys og samhold i institusjoner</li>
    </ul>
  </section>

  <div class="pager">
    <svg class="pager-arrow" viewBox="0 0 22 14"><path d="M0 7h20M14 1l6 6-6 6" stroke="#2b2b2b" stroke-width="1.4" fill="none"/></svg>
    <span class="pager-current">02</span>
    <span class="pager-total">/04</span>
  </div>
</body>
</html>
```